Real Estate agent needs flyer/folder to contain bio and overview of services

I'm including files of the layout of the small folder. The folder is 6 1/2 across and 9 1/2 inches long. It will have a front & back cover and then writing on the 2 inside pages.

I am sending a few files to incorporate into the flyer, 1 new logo to use and 2 files which are coloring ideas.

```html
<!DOCTYPE html>
<html lang="en">
<head>
<meta charset="utf-8">
<title>Dana Morelli – Folder Covers</title>
<link rel="stylesheet" href="https://fonts.googleapis.com/css2?family=Montserrat:wght@400;500;600&display=swap">
<style>
  :root {
    --stage: #b9b9b9;
    --silver-light: #f4f5f6;
    --silver-mid: #dcdee1;
    --silver-dark: #c3c6ca;
    --brand-blue: #1b5fd6;
    --band-blue: #3d67b5;
    --band-mid: #2f55a3;
    --navy: #183573;
    --ink: #1c1c1c;
    --badge: #a9b7d6;
  }
  * { margin: 0; padding: 0; box-sizing: border-box; }
  html, body { width: 917px; height: 1200px; overflow: hidden; }
  body {
    background: var(--stage);
    font-family: "Montserrat", sans-serif;
    position: relative;
  }
  .folder-cover {
    position: absolute;
    top: 237px;
    width: 430px;
    height: 726px;
    overflow: hidden;
    box-shadow: 0 3px 8px rgba(0,0,0,0.35);
  }
  .folder-cover--front { left: 19px; }
  .folder-cover--back { left: 468px; }
  .cover-art { position: absolute; inset: 0; width: 100%; height: 100%; }

  .brand-name {
    position: absolute;
    left: 0; right: 0;
    text-align: center;
    color: var(--brand-blue);
    font-weight: 500;
    letter-spacing: 0.06em;
    line-height: 1.15;
  }
  .folder-cover--front .brand-name { top: 240px; font-size: 34px; }
  .folder-cover--back .brand-name { top: 205px; font-size: 26px; }

  .tagline {
    position: absolute;
    top: 472px; left: 0; right: 0;
    text-align: center;
    color: var(--brand-blue);
    font-weight: 600;
    font-size: 12.5px;
    letter-spacing: 0.05em;
  }
  .tagline-url {
    position: absolute;
    top: 494px; left: 0; right: 0;
    text-align: center;
    color: var(--ink);
    font-weight: 500;
    font-size: 8px;
    letter-spacing: 0.3em;
  }

  .agent-photo {
    position: absolute;
    left: 113px; top: 358px;
    width: 74px; height: 74px;
    border-radius: 50%;
    background: radial-gradient(circle at 50% 40%, #e3c79a 0%, #b99a6e 40%, #1b5fd6 72%);
  }
  .agent-contact {
    position: absolute;
    left: 197px; top: 363px;
    color: var(--brand-blue);
  }
  .agent-contact__name {
    font-weight: 600;
    font-size: 11.5px;
    margin-bottom: 6px;
    letter-spacing: -0.01em;
  }
  .agent-contact__line {
    display: flex;
    align-items: center;
    gap: 7px;
    font-size: 8px;
    height: 14px;
  }
  .agent-contact__line svg { width: 9px; height: 9px; flex: none; }

  .agent-bio {
    position: absolute;
    top: 479px; left: 60px; right: 60px;
    text-align: center;
    font-size: 6.3px;
    line-height: 1.3;
    color: var(--ink);
  }

  .brokerage {
    position: absolute;
    left: 18px; top: 672px;
    display: flex;
    align-items: center;
    gap: 6px;
    color: #ffffff;
    font-weight: 600;
    font-size: 10px;
    letter-spacing: 0.03em;
  }
  .brokerage__dot {
    width: 10px; height: 10px;
    border-radius: 50%;
    background: #ffffff;
  }
  .partner-badges {
    position: absolute;
    right: 14px; top: 666px;
    display: flex;
    gap: 10px;
  }
  .partner-badge {
    width: 24px; height: 24px;
    background: var(--badge);
    opacity: 0.85;
  }
</style>
</head>
<body>

<section class="folder-cover folder-cover--front">
  <svg class="cover-art" viewBox="0 0 430 726" preserveAspectRatio="none" aria-hidden="true">
    <defs>
      <linearGradient id="silverFront" x1="0" y1="0" x2="1" y2="1">
        <stop offset="0" stop-color="#c9ccd0"/>
        <stop offset="0.45" stop-color="#eef0f2"/>
        <stop offset="1" stop-color="#d6d9dc"/>
      </linearGradient>
    </defs>
    <rect width="430" height="726" fill="url(#silverFront)"/>
    <g fill="#ffffff" opacity="0.45">
      <polygon points="0,40 150,0 200,0 0,90"/>
      <polygon points="20,300 220,90 420,300 220,500"/>
    </g>
    <g fill="none" stroke="#ffffff" stroke-width="2" opacity="0.7">
      <polyline points="30,300 220,110 410,300 220,490 30,300"/>
    </g>
    <path d="M306,0 C420,120 440,330 360,560 L430,560 L430,0 Z" fill="var(--navy)"/>
    <path d="M0,503 C110,520 220,550 300,562 C360,548 400,530 430,520 L430,726 L0,726 Z" fill="var(--band-blue)"/>
    <path d="M0,600 C140,630 260,690 430,600 L430,726 L0,726 Z" fill="var(--band-mid)"/>
    <path d="M180,726 C280,700 360,640 430,560 L430,726 Z" fill="var(--navy)"/>
  </svg>
  <div class="brand-name">DANA<br>MORELLI</div>
  <p class="tagline">FINE HOMES &amp; LUXURY PROPERTIES</p>
  <p class="tagline-url">www.danamhomes.com</p>
</section>

<section class="folder-cover folder-cover--back">
  <svg class="cover-art" viewBox="0 0 430 726" preserveAspectRatio="none" aria-hidden="true">
    <defs>
      <linearGradient id="silverBack" x1="1" y1="0" x2="0" y2="1">
        <stop offset="0" stop-color="#c9ccd0"/>
        <stop offset="0.45" stop-color="#eef0f2"/>
        <stop offset="1" stop-color="#d6d9dc"/>
      </linearGradient>
    </defs>
    <rect width="430" height="726" fill="url(#silverBack)"/>
    <g fill="#ffffff" opacity="0.45">
      <polygon points="430,40 280,0 230,0 430,90"/>
      <polygon points="15,235 215,35 415,235 215,435"/>
    </g>
    <g fill="none" stroke="#ffffff" stroke-width="2" opacity="0.7">
      <polyline points="25,235 215,45 405,235 215,425 25,235"/>
    </g>
    <path d="M0,518 C140,540 230,560 260,548 C330,530 390,510 430,500 L430,726 L0,726 Z" fill="var(--band-blue)"/>
    <path d="M0,726 L0,640 C120,690 250,720 330,726 Z" fill="var(--navy)"/>
  </svg>
  <div class="brand-name">DANA<br>MORELLI</div>

  <div class="agent-photo" role="img" aria-label="Portrait photo of the agent"></div>
  <div class="agent-contact">
    <p class="agent-contact__name">DANA MORELLI</p>
    <p class="agent-contact__line">
      <svg viewBox="0 0 10 10"><circle cx="5" cy="5" r="4.4" fill="none" stroke="currentColor" stroke-width="0.8"/><path d="M3.4,3 l0.9,-0.3 l0.5,1.2 l-0.5,0.4 a3,3 0 0 0 1.2,1.2 l0.4,-0.5 l1.2,0.5 l-0.3,0.9 a3.6,3.6 0 0 1 -3.4,-3.4 z" fill="currentColor"/></svg>
      555 014 2876
    </p>
    <p class="agent-contact__line">
      <svg viewBox="0 0 10 10"><circle cx="5" cy="5" r="4.4" fill="none" stroke="currentColor" stroke-width="0.8"/><rect x="2.8" y="3.4" width="4.4" height="3.2" fill="none" stroke="currentColor" stroke-width="0.7"/><path d="M2.8,3.4 L5,5.2 L7.2,3.4" fill="none" stroke="currentColor" stroke-width="0.7"/></svg>
      dana@danamhomes.com
    </p>
    <p class="agent-contact__line">
      <svg viewBox="0 0 10 10"><circle cx="5" cy="5" r="4.4" fill="none" stroke="currentColor" stroke-width="0.8"/><circle cx="5" cy="5" r="2.6" fill="none" stroke="currentColor" stroke-width="0.6"/><path d="M2.4,5 H7.6 M5,2.4 V7.6" stroke="currentColor" stroke-width="0.6"/></svg>
      www.danamhomes.com
    </p>
  </div>

  <p class="agent-bio">Along with being your Realtor, I'm a lifelong resource for all things home-related &amp; beyond...if you need a great referral for anything at all, call me! &nbsp;I can't wait to work with you!</p>

  <div class="brokerage"><span class="brokerage__dot"></span>Summit Realty</div>
  <div class="partner-badges">
    <span class="partner-badge"></span>
    <span class="partner-badge"></span>
  </div>
</section>

</body>
</html>
```